Sidebar ad for rare disease patient registries

We have a product (ENGAGE) that allows patient advocacy foundations to promote our patient registries while maintaining their own branding. We need a sidebar ad and banner ad designed that we could provide to the advocacy organizations to post on their own websites. The advocacy groups get a unique URL from us and they promote this URL to their disease community. When a user clicks the link, we change the branding on our site to reflect the advocacy organization's branding.

Having the ability to have a quality graphical ad on their foundation webpages that entice their patient community to join our registries is be critical. Looking for something about 230 px wide by 500 px tall.

We would provide multiple different text messages on the ads, so need room to have a headline and maybe a short sentence and a button that users would push to 'ENGAGE' to join the patient registry.

Would like a stylized button with the word ENGAGE on it which would take the user to our registry. Possibly include the caremeadowline logo in the button / graphic somehow in a tasteful way. CareMeadowline operates the technology and registry program, but we don't want to overtly brand ourselves but would like to include our brand if possible. We can not get between the advocacy organizations and the patient community. This is very much about trust with the patient community and asking them to share detailed medical history. They will not be sharing their information with CareMeadowline, but rather the advocacy organization that will have this ad on their website.

Would eventually like a series of graphics that an advocacy organization could choose from.

Example tag lines:

Give future generations a precious gift: your medical information

Give the global patient community the gift of your participation

Help researchers to help patients: Participate in trials and studies

Help researchers help you: Join our patient registry

The more researchers know about patients, the sooner they can find answers

Joining the patient registry helps the global patient community

Make your medical information count! Join the [your disease] registry

Pharma can’t invest in research if they don’t know how many patients have [your disease]. Help us build our patient registry.

There’s power in numbers. Help us build our patient registry.

Why participate in the [your disease] registry? Raise the visibility of [your disease] and generate more research interest.

FYI, our logo can be found at http://www.caremeadowline-example.com/templates/ja_social/images/logo.png

Also, we would prefer images that reflect patients as opposed to healthcare professionals if possible and please mention the words Patient Registry in the text.

Target Market(s)

Disease foundations and patient advocacy organizations. For example:
http://www.renalhopealliance-example.org
http://www.ifacepressure-example.com/
http://www.milosfreshstart-example.org
http://www.familyeffortnm-example.org
http://www.musclefadeunion-example.org

Industry/Entity Type

Product

```html
<!DOCTYPE html>
<html lang="en">
<head>
<meta charset="utf-8">
<title>Join the Registry – Sidebar Ads</title>
<link rel="stylesheet" href="https://fonts.googleapis.com/css2?family=Cabin+Condensed:wght@600&family=Open+Sans:wght@300&family=Delius&family=Cabin:wght@500&display=swap">
<style>
  :root {
    --stage: #626b73;
    --card-edge: #d5d9dd;
    --card-top: #f3f4f6;
    --card-bottom: #e8ebee;
    --green-light: #8fd131;
    --green-dark: #57a514;
    --blue-light: #3da4f0;
    --blue-dark: #0e72d2;
    --headline: #2b95e6;
    --tagline: #3b3f44;
    --photo-paper: #eceeef;
    --photo-shade: #b9bdc2;
    --photo-deep: #8d9197;
    --white: #ffffff;
  }
  * { box-sizing: border-box; margin: 0; padding: 0; }
  html, body { width: 1200px; height: 900px; overflow: hidden; }
  body { background: var(--stage); position: relative; }

  .sidebar-ad {
    position: absolute;
    top: 75px;
    width: 345px;
    height: 750px;
    border: 2px solid var(--card-edge);
    background: linear-gradient(to bottom, var(--card-top), var(--card-bottom));
    overflow: hidden;
  }
  .sidebar-ad--green { left: 217px; }
  .sidebar-ad--blue  { left: 613px; }

  .ad-photo {
    position: absolute;
    left: 0; top: 80px;
    width: 100%; height: 330px;
    background: linear-gradient(150deg, var(--photo-deep) 0%, var(--photo-shade) 30%, var(--photo-paper) 65%, var(--photo-shade) 100%);
    -webkit-mask-image: linear-gradient(to bottom, #000 65%, transparent 100%);
    mask-image: linear-gradient(to bottom, #000 65%, transparent 100%);
  }

  .ad-header { position: absolute; left: 0; top: 0; width: 100%; height: 140px; }
  .ad-header__title {
    position: absolute; left: 0; top: 17px; width: 100%;
    text-align: center;
    font-family: "Cabin Condensed", sans-serif;
    font-weight: 600;
    font-size: 33px;
    letter-spacing: 0.5px;
    color: var(--white);
    text-shadow: 0 1px 2px rgba(0,0,0,0.25);
  }

  .ad-headline {
    position: absolute; left: 19px; top: 417px;
    font-family: "Open Sans", sans-serif;
    font-weight: 300;
    font-size: 46px;
    line-height: 50px;
    color: var(--headline);
    letter-spacing: -0.5px;
    white-space: nowrap;
  }
  .ad-tagline {
    position: absolute; left: 19px; top: 572px;
    font-family: "Delius", cursive;
    font-size: 27px;
    color: var(--tagline);
    white-space: nowrap;
  }

  .engage-button { position: absolute; left: 36px; top: 648px; width: 270px; height: 72px; }
  .engage-button__label {
    position: absolute; left: 76px; top: 18px;
    font-family: "Cabin", sans-serif;
    font-weight: 500;
    font-size: 30px;
    letter-spacing: 1px;
    color: var(--white);
    text-shadow: 0 1px 1px rgba(0,0,0,0.2);
  }
</style>
</head>
<body>

  <section class="sidebar-ad sidebar-ad--green">
    <div class="ad-photo" role="img" aria-label="Photo of a blood test results sheet with a pen and a stethoscope lying on it"></div>
    <svg class="ad-header" viewBox="0 0 345 140" aria-hidden="true">
      <defs>
        <linearGradient id="band-green" x1="0" y1="0" x2="0" y2="1">
          <stop offset="0" stop-color="#8fd131"/>
          <stop offset="1" stop-color="#57a514"/>
        </linearGradient>
      </defs>
      <path d="M0 0 H345 V74 Q180 70 0 102 Z" fill="url(#band-green)"/>
      <path d="M0 102 Q180 70 345 74 V86 Q180 82 0 118 Z" fill="#ffffff"/>
    </svg>
    <div class="ad-header__title">JOIN THE REGISTRY</div>
    <p class="ad-headline">Give future<br>generations<br>a precious gift</p>
    <p class="ad-tagline">your medical information</p>
    <a class="engage-button" href="#">
      <svg width="270" height="72" viewBox="0 0 270 72" aria-hidden="true">
        <defs>
          <linearGradient id="btn-green" x1="0" y1="0" x2="0" y2="1">
            <stop offset="0" stop-color="#9bd83a"/>
            <stop offset="1" stop-color="#4f9c12"/>
          </linearGradient>
        </defs>
        <path d="M30 12 H240 L262 39 L240 66 H30 Z" fill="url(#btn-green)"/>
        <circle cx="34" cy="38" r="26" fill="#ffffff"/>
        <circle cx="34" cy="38" r="16" fill="#57a514"/>
      </svg>
      <span class="engage-button__label">ENGAGE</span>
    </a>
  </section>

  <section class="sidebar-ad sidebar-ad--blue">
    <div class="ad-photo" role="img" aria-label="Photo of a blood test results sheet with a pen and a stethoscope lying on it"></div>
    <svg class="ad-header" viewBox="0 0 345 140" aria-hidden="true">
      <defs>
        <linearGradient id="band-blue" x1="0" y1="0" x2="0" y2="1">
          <stop offset="0" stop-color="#3da4f0"/>
          <stop offset="1" stop-color="#0e72d2"/>
        </linearGradient>
      </defs>
      <path d="M0 0 H345 V74 Q180 70 0 102 Z" fill="url(#band-blue)"/>
      <path d="M0 102 Q180 70 345 74 V86 Q180 82 0 118 Z" fill="#ffffff"/>
    </svg>
    <div class="ad-header__title">JOIN THE REGISTRY</div>
    <p class="ad-headline">Give future<br>generations<br>a precious gift</p>
    <p class="ad-tagline">your medical information</p>
    <a class="engage-button" href="#">
      <svg width="270" height="72" viewBox="0 0 270 72" aria-hidden="true">
        <defs>
          <linearGradient id="btn-green-2" x1="0" y1="0" x2="0" y2="1">
            <stop offset="0" stop-color="#9bd83a"/>
            <stop offset="1" stop-color="#4f9c12"/>
          </linearGradient>
        </defs>
        <path d="M30 12 H240 L262 39 L240 66 H30 Z" fill="url(#btn-green-2)"/>
        <circle cx="34" cy="38" r="26" fill="#ffffff"/>
        <circle cx="34" cy="38" r="16" fill="#57a514"/>
      </svg>
      <span class="engage-button__label">ENGAGE</span>
    </a>
  </section>

</body>
</html>
```